Summer Sale Graphics for Social Media

I want to create 11 social media graphics (new Instagram size 4:5 (1080 x 1350 pixels) focusing on our Summer Sale Graphics, using any of the pics attached. Use the attached pics, NO RANDOM STOCK PHOTOGRAPHY. For the color scheme of the graphics, they should all be complementary to the product colors in the photos.
You can add any of the photos attached but none are required. You can do some of the graphics in all text. I mainly need BOLD text that says one of the headlines (11 total) SEE ATTACHED WORD DOCUMENT for the headlines to use.

```html
<!DOCTYPE html>
<html lang="en">
<head>
<meta charset="utf-8">
<title>Summer Sale Social Graphics</title>
<link href="https://fonts.googleapis.com/css2?family=Oswald:wght@600;700&family=Inter:wght@400;700&display=swap" rel="stylesheet">
<style>
  :root {
    --board: #1b1b1b;
    --paper: #ffffff;
    --magenta: #c7127f;
    --pink: #ea8ee4;
    --ink: #1a1a1a;
    --bottle-top: #f4f3f1;
    --bottle-bottom: #d9d6d3;
    --photo-top: #d9b8a3;
    --photo-mid: #b88466;
    --photo-bottom: #2a2426;
  }
  * { margin: 0; padding: 0; box-sizing: border-box; }
  html, body { width: 1200px; height: 1200px; overflow: hidden; background: var(--board); }
  .board {
    position: absolute; left: 0; top: 0;
    width: 1932px; height: 1932px;
    transform: scale(0.62112); transform-origin: 0 0;
    background: var(--board);
  }
  .panel {
    position: absolute; width: 447px; height: 559px;
    background: var(--paper); overflow: hidden;
    font-family: "Oswald", "Arial Narrow", sans-serif;
    color: var(--magenta);
  }
  .swoosh { position: absolute; left: 0; top: 0; width: 447px; height: 559px; }
  .headline {
    position: absolute; font-weight: 700; text-transform: uppercase;
    line-height: 1.08; letter-spacing: 0; white-space: nowrap; z-index: 2;
  }
  .headline.centered { text-align: center; }
  .sale-banner {
    position: absolute; height: 58px; z-index: 2;
    background: var(--magenta); color: var(--paper);
    font-weight: 700; font-size: 36px; line-height: 58px; text-align: center;
    text-transform: uppercase; white-space: nowrap;
    transform: rotate(-6deg);
  }
  .discount {
    position: absolute; font-family: "Inter", Arial, sans-serif; z-index: 2;
    font-weight: 700; font-size: 21px; color: var(--magenta); white-space: nowrap;
  }
  .discount .to { font-weight: 400; color: var(--ink); }
  .product-photo {
    position: absolute; border-radius: 10px;
    background: linear-gradient(180deg, var(--bottle-top), var(--bottle-bottom));
  }
  .model-photo {
    position: absolute; border-radius: 80px 80px 0 0; z-index: 1;
    background: linear-gradient(180deg, var(--photo-top) 0%, var(--photo-mid) 45%, var(--photo-bottom) 100%);
  }
  .model-photo.light {
    background: linear-gradient(180deg, var(--photo-top) 0%, #f1eeee 40%, #e9e6e6 65%, var(--photo-bottom) 100%);
  }
</style>
</head>
<body>
<div class="board">

  <!-- Row 1 -->
  <section class="panel" style="left:34px; top:80px;">
    <svg class="swoosh" viewBox="0 0 447 559"><path d="M0,470 C160,490 330,455 447,385 L447,402 C320,472 150,500 0,484Z" fill="var(--pink)"/><path d="M0,484 C150,500 320,472 447,402 L447,559 L0,559Z" fill="var(--magenta)"/></svg>
    <div class="headline centered" style="left:20px; top:105px; width:315px; font-size:35px;">Your summer body<br>won’t wait</div>
    <div class="sale-banner" style="left:60px; top:195px; width:225px;">Sale now!</div>
    <div class="discount" style="left:105px; top:268px;">Up <span class="to">to</span> $15 OFF</div>
    <div class="product-photo" role="img" aria-label="Row of four supplement bottles" style="left:22px; top:420px; width:240px; height:100px;"></div>
    <div class="model-photo" role="img" aria-label="Smiling woman in a brown top holding supplement bottles" style="left:290px; top:135px; width:157px; height:424px;"></div>
  </section>

  <section class="panel" style="left:508px; top:80px;">
    <svg class="swoosh" viewBox="0 0 447 559"><path d="M0,470 C160,490 330,455 447,385 L447,402 C320,472 150,500 0,484Z" fill="var(--pink)"/><path d="M0,484 C150,500 320,472 447,402 L447,559 L0,559Z" fill="var(--magenta)"/></svg>
    <svg style="position:absolute; left:142px; top:78px;" width="68" height="68" viewBox="0 0 68 68" aria-hidden="true"><circle cx="34" cy="34" r="30" fill="none" stroke="var(--magenta)" stroke-width="5"/><path d="M34 14 V34 H44" fill="none" stroke="var(--magenta)" stroke-width="4"/></svg>
    <div class="headline centered" style="left:20px; top:160px; width:315px; font-size:36px;">Final countdown<br>to summer</div>
    <div class="sale-banner" style="left:62px; top:250px; width:230px;">Sale now!</div>
    <div class="discount" style="left:105px; top:325px;">Up <span class="to">to</span> $15 OFF</div>
    <div class="product-photo" role="img" aria-label="Row of four supplement bottles" style="left:40px; top:395px; width:220px; height:125px;"></div>
    <div class="model-photo light" role="img" aria-label="Smiling woman in a white sweater holding a supplement bottle" style="left:300px; top:210px; width:147px; height:349px;"></div>
  </section>

  <section class="panel" style="left:982px; top:80px;">
    <svg class="swoosh" viewBox="0 0 447 559"><path d="M0,470 C160,490 330,455 447,385 L447,402 C320,472 150,500 0,484Z" fill="var(--pink)"/><path d="M0,484 C150,500 320,472 447,402 L447,559 L0,559Z" fill="var(--magenta)"/></svg>
    <div class="headline centered" style="left:20px; top:85px; width:345px; font-size:35px;">Detox, burn fat,<br>and turn heads<br>this summer</div>
    <div class="sale-banner" style="left:62px; top:222px; width:230px;">Sale now!</div>
    <div class="discount" style="left:102px; top:296px;">Up <span class="to">to</span> $15 OFF</div>
    <div class="product-photo" role="img" aria-label="Row of four supplement bottles" style="left:40px; top:395px; width:220px; height:125px;"></div>
    <div class="model-photo light" role="img" aria-label="Smiling woman in a white sweater holding a supplement bottle" style="left:300px; top:210px; width:147px; height:349px;"></div>
  </section>

  <section class="panel" style="left:1456px; top:80px;">
    <svg class="swoosh" viewBox="0 0 447 559"><path d="M0,470 C160,490 330,455 447,385 L447,402 C320,472 150,500 0,484Z" fill="var(--pink)"/><path d="M0,484 C150,500 320,472 447,402 L447,559 L0,559Z" fill="var(--magenta)"/></svg>
    <div class="headline" style="left:30px; top:82px; font-size:30px;">Summer’s here.<br>And we’re having<br><span style="font-size:24px;">the</span> <span style="font-size:40px;">biggest sale</span><br><span style="font-size:24px;">of</span> <span style="font-size:40px;">the year</span></div>
    <div class="discount" style="left:30px; top:235px;">Up <span class="to">to</span> $15 OFF</div>
    <div class="product-photo" role="img" aria-label="Group of four supplement bottles" style="left:25px; top:295px; width:180px; height:100px;"></div>
    <div class="model-photo light" role="img" aria-label="Smiling woman in a white cropped sweater" style="left:225px; top:225px; width:170px; height:334px;"></div>
    <div class="product-photo" role="img" aria-label="Row of skincare and supplement products" style="left:175px; top:490px; width:255px; height:69px; z-index:2;"></div>
  </section>

  <!-- Row 2 -->
  <section class="panel" style="left:34px; top:680px;">
    <svg class="swoosh" viewBox="0 0 447 559"><path d="M0,470 C160,490 330,455 447,385 L447,402 C320,472 150,500 0,484Z" fill="var(--pink)"/><path d="M0,484 C150,500 320,472 447,402 L447,559 L0,559Z" fill="var(--magenta)"/></svg>
    <div class="headline centered" style="left:40px; top:100px; width:367px; font-size:34px;">One sale. One body.<br>One summer to slay</div>
    <div class="product-photo" role="img" aria-label="Group of four supplement bottles" style="left:40px; top:400px; width:175px; height:100px;"></div>
    <div class="model-photo" role="img" aria-label="Smiling woman in a brown top holding supplement bottles" style="left:245px; top:190px; width:195px; height:369px;"></div>
  </section>

  <section class="panel" style="left:508px; top:680px;">
    <svg class="swoosh" viewBox="0 0 447 559"><path d="M0,470 C160,490 330,455 447,385 L447,402 C320,472 150,500 0,484Z" fill="var(--pink)"/><path d="M0,484 C150,500 320,472 447,402 L447,559 L0,559Z" fill="var(--magenta)"/></svg>
    <div class="headline" style="left:30px; top:140px; font-size:34px;">Summer isn’t waiting<br>neither should you</div>
    <div class="sale-banner" style="left:35px; top:230px; width:235px; transform:rotate(-2deg);">Sale now!</div>
    <div class="discount" style="left:52px; top:298px;">Up <span class="to">to</span> $15 OFF</div>
    <div class="product-photo" role="img" aria-label="Row of four supplement bottles" style="left:30px; top:390px; width:215px; height:120px;"></div>
    <div class="model-photo light" role="img" aria-label="Smiling woman in a white sweater holding a supplement bottle" style="left:285px; top:210px; width:162px; height:349px;"></div>
  </section>

  <section class="panel" style="left:982px; top:680px;">
    <svg class="swoosh" viewBox="0 0 447 559"><path d="M0,470 C160,490 330,455 447,385 L447,402 C320,472 150,500 0,484Z" fill="var(--pink)"/><path d="M0,484 C150,500 320,472 447,402 L447,559 L0,559Z" fill="var(--magenta)"/></svg>
    <div class="headline" style="left:28px; top:60px; font-size:37px; line-height:1.05;">Slim waist.<br>Flat tummy.<br>More energy.</div>
    <div class="headline" style="left:28px; top:188px; font-size:46px;">Let’s go!</div>
    <div class="sale-banner" style="left:25px; top:270px; width:210px; font-size:32px;">Sale now!</div>
    <div class="discount" style="left:52px; top:336px;">Up <span class="to">to</span> $15 OFF</div>
    <div class="product-photo" role="img" aria-label="Row of four supplement bottles" style="left:30px; top:392px; width:220px; height:118px;"></div>
    <div class="model-photo" role="img" aria-label="Smiling woman in a brown top holding supplement bottles" style="left:275px; top:90px; width:165px; height:469px;"></div>
  </section>

  <section class="panel" style="left:1456px; top:680px;">
    <svg class="swoosh" viewBox="0 0 447 559"><path d="M0,470 C160,490 330,455 447,385 L447,402 C320,472 150,500 0,484Z" fill="var(--pink)"/><path d="M0,484 C150,500 320,472 447,402 L447,559 L0,559Z" fill="var(--magenta)"/></svg>
    <div class="headline" style="left:28px; top:105px; font-size:58px;">Hurry!</div>
    <div class="headline" style="left:28px; top:168px; font-size:31px;">Our summer slim-down<br>sale is on</div>
    <div class="headline" style="left:28px; top:250px; font-size:35px;">Don’t miss it!</div>
    <div class="product-photo" role="img" aria-label="Row of four supplement bottles" style="left:30px; top:390px; width:215px; height:120px;"></div>
    <div class="model-photo light" role="img" aria-label="Smiling woman in a white sweater holding a supplement bottle" style="left:330px; top:210px; width:117px; height:349px;"></div>
  </section>

  <!-- Row 3 -->
  <section class="panel" style="left:220px; top:1270px;">
    <svg class="swoosh" viewBox="0 0 447 559"><path d="M0,470 C160,490 330,455 447,385 L447,402 C320,472 150,500 0,484Z" fill="var(--pink)"/><path d="M0,484 C150,500 320,472 447,402 L447,559 L0,559Z" fill="var(--magenta)"/></svg>
    <div class="sale-banner" style="left:28px; top:110px; width:150px; height:70px; line-height:70px; font-size:56px;">Sale</div>
    <div class="headline" style="left:27px; top:198px; font-size:36px;">Your summer body<br>starts here</div>
    <div class="product-photo" role="img" aria-label="Row of four supplement bottles" style="left:30px; top:390px; width:215px; height:120px;"></div>
    <div class="model-photo light" role="img" aria-label="Smiling woman in a white sweater holding a supplement bottle" style="left:290px; top:292px; width:157px; height:267px;"></div>
  </section>

  <section class="panel" style="left:699px; top:1270px;">
    <svg class="swoosh" viewBox="0 0 447 559"><path d="M0,470 C160,490 330,455 447,385 L447,402 C320,472 150,500 0,484Z" fill="var(--pink)"/><path d="M0,484 C150,500 320,472 447,402 L447,559 L0,559Z" fill="var(--magenta)"/></svg>
    <div class="headline" style="left:27px; top:72px; font-size:42px; line-height:1.02;">Limited<br>time summer sale</div>
    <div class="headline" style="left:27px; top:162px; font-size:34px;">Snatch your<br>supplements now!</div>
    <div class="product-photo" role="img" aria-label="Row of four supplement bottles" style="left:25px; top:420px; width:235px; height:100px;"></div>
    <div class="model-photo" role="img" aria-label="Smiling woman in a brown top holding supplement bottles" style="left:280px; top:255px; width:160px; height:304px;"></div>
  </section>

  <section class="panel" style="left:1178px; top:1270px;">
    <svg class="swoosh" viewBox="0 0 447 559"><path d="M0,470 C160,490 330,455 447,385 L447,402 C320,472 150,500 0,484Z" fill="var(--pink)"/><path d="M0,484 C150,500 320,472 447,402 L447,559 L0,559Z" fill="var(--magenta)"/></svg>
    <div class="headline centered" style="left:10px; top:80px; width:427px; font-size:33px;">Get snatched for summer<br>supplements on</div>
    <div class="headline centered" style="left:10px; top:160px; width:427px; font-size:46px;">Sale now!</div>
    <div class="product-photo" role="img" aria-label="Row of four supplement bottles" style="left:25px; top:420px; width:235px; height:100px;"></div>
    <div class="model-photo light" role="img" aria-label="Smiling woman in a white sweater holding a supplement bottle" style="left:280px; top:225px; width:167px; height:334px;"></div>
  </section>

</div>
</body>
</html>
```